Design a helpdesk ticketing platform *

We are launching a helpdesk ticketing platform. Very much like lumidesk.example, brightowl.example, calmhub.example, tidyqueue.example etc. We have a full mid-fidelity prototype built and we want someone to build the full fidelity of the product.

You can view the full mid-fidelity prototype here: https://shortlink.example/Qw8pLk

The best way moving forward is to just design the following 4 pages

- Main Dashboard https://shortlink.example/48vRxN
- All tickets https://shortlink.example/jbdYsW
- Viewing a ticket https://shortlink.example/mHqLtB
- Contacts https://shortlink.example/yKeoPd

Target Market(s)

Small business owners

Industry/Entity Type

Saas

Number of Pages Required

4 page

Font styles to use
Serif
Sans Serif

Colors

Designer to choose colors to be used in the design.

Requirements
Must have
• Must follow the prototype exactly. We are not looking for any UX changes. We want the designe xactly as the prototype is. We are only looking for design ideas.
Should not have
• modern, clean. We'd love to see the primary color as yellow, purple, orange, green or blue. You choose which one you think looks best and go with that.

```html
<!DOCTYPE html>
<html lang="en">
<head>
<meta charset="utf-8">
<title>Ticketnest – New Ticket</title>
<link href="https://fonts.googleapis.com/css2?family=Poppins:wght@400;500;600&display=swap" rel="stylesheet">
<style>
:root{
  --orange-deep:#f4672c;
  --orange:#fb9f31;
  --orange-soft:#fdb046;
  --purple:#5a3fe0;
  --purple-dark:#4a2fc4;
  --navy:#1f1c4d;
  --muted:#6f6d80;
  --placeholder:#a9a8b5;
  --line:#e8e8ee;
  --panel:#f6f6f8;
  --field-head:#e6e6e9;
  --white:#ffffff;
}
*{box-sizing:border-box;margin:0;padding:0}
html,body{width:1200px;height:700px;overflow:hidden}
body{font-family:"Poppins",sans-serif;color:var(--navy);background:var(--panel)}
.app{display:flex;width:1200px;height:700px}

/* Sidebar */
.sidebar{width:250px;background:var(--orange);position:relative;overflow:hidden}
.brand{height:54px;background:var(--orange-deep);display:flex;align-items:center;justify-content:space-between;padding:0 10px 0 52px}
.brand-name{color:var(--white);font-size:21px;font-weight:400}
.brand-toggle{width:14px;display:flex;flex-direction:column;gap:4px}
.brand-toggle span{height:1px;background:rgba(255,255,255,.6)}
.new-ticket{margin:32px 20px 0;height:31px;border-radius:16px;background:var(--purple);color:var(--white);display:flex;align-items:center;justify-content:space-between;padding:0 12px 0 14px;font-size:12px;font-weight:500;letter-spacing:.2px}
.kebab{display:flex;flex-direction:column;gap:2px}
.kebab span{width:3px;height:3px;border-radius:50%;background:rgba(255,255,255,.8)}
.nav{margin:38px 20px 0;background:var(--white);border-radius:8px;padding:8px 0 34px;position:relative;z-index:1}
.nav-item{display:flex;align-items:center;height:43px;padding:0 16px 0 18px;font-size:12px;letter-spacing:.3px;color:var(--navy);border-bottom:1px solid #eeeef2}
.nav-item:last-child{border-bottom:none}
.nav-item svg{width:20px;height:20px;margin-right:14px;flex:none}
.nav-item .chev{margin-left:auto;width:10px;height:10px;margin-right:0}
.nav-item.active{color:var(--purple);font-weight:600}
.sidebar-art{position:absolute;left:0;right:0;bottom:0;height:250px;background:linear-gradient(160deg,rgba(253,176,70,0) 0%,var(--orange-soft) 55%,rgba(246,140,40,.6) 100%)}

/* Main */
.main{flex:1;position:relative;padding:0 25px}
.topbar{height:54px;display:flex;align-items:center;justify-content:space-between}
.crumbs{font-size:12px;font-weight:500;padding-top:2px}
.crumbs .sep{color:var(--placeholder);margin:0 5px}
.top-tools{display:flex;align-items:center;gap:10px}
.search{width:145px;height:29px;border:1.5px solid #8fb4d8;border-radius:15px;display:flex;align-items:center;justify-content:space-between;padding:0 8px 0 12px;font-size:10px;color:var(--placeholder)}
.avatar{width:36px;height:36px;border-radius:50%;background:var(--purple);color:var(--white);display:flex;align-items:center;justify-content:center;font-size:14px;font-weight:500}
.page-title{font-size:21px;font-weight:500;margin-top:6px;display:inline-block;position:relative;padding-bottom:3px}
.page-title::after{content:"";position:absolute;left:0;bottom:-3px;width:46px;height:2px;background:var(--purple)}
.lead{font-size:12px;color:var(--muted);margin-top:26px}

.form{margin-top:20px;background:var(--white);border-radius:6px;box-shadow:0 1px 3px rgba(31,28,77,.06);overflow:hidden}
.row-to{height:42px;background:var(--field-head);display:flex;align-items:center;padding:0 16px;font-size:13px;font-weight:500}
.row-to .drop{margin-left:auto;margin-right:28px}
.to-links{font-size:13px}
.to-links .bar{color:var(--placeholder);margin:0 4px}
.row{border-bottom:1px solid var(--line);padding:0 16px}
.row-subject{height:43px;display:flex;align-items:center;font-size:13px;font-weight:500}
.row-meta{height:89px;display:grid;grid-template-columns:repeat(4,1fr);gap:16px;padding:14px 16px 0 13px}
.field label{display:block;font-size:11px;font-weight:500;margin-bottom:5px;padding-left:3px}
.select{height:29px;border:1px solid #dedee4;border-radius:15px;display:flex;align-items:center;justify-content:space-between;padding:0 10px 0 12px;font-size:10px;color:var(--placeholder)}
.row-desc{height:212px;padding-top:16px;font-size:13px;font-weight:500}
.row-actions{height:68px;display:flex;align-items:center;gap:16px}
.row-actions svg{width:20px;height:20px}
.another{margin-left:auto;display:flex;align-items:center;font-size:11px;color:var(--muted)}
.checkbox{width:13px;height:13px;border:1.5px solid var(--purple);border-radius:2px;margin-right:7px}
.trash{margin:0 6px 0 8px}
.btn-create{height:30px;padding:0 16px;border-radius:15px;background:linear-gradient(90deg,var(--purple-dark),var(--purple));color:var(--white);font-size:12.5px;font-weight:500;display:flex;align-items:center}
.row-tags{height:38px;display:flex;align-items:center;gap:8px;font-size:13px;font-weight:500;border-bottom:none}
.tag-add{background:#cfcfd6;color:var(--white);font-size:9px;padding:3px 6px;font-weight:400}
</style>
</head>
<body>
<div class="app">
  <aside class="sidebar">
    <div class="brand">
      <span class="brand-name">Ticketnest</span>
      <div class="brand-toggle"><span></span><span></span><span></span><span></span></div>
    </div>
    <div class="new-ticket">NEW TICKET<div class="kebab"><span></span><span></span><span></span></div></div>
    <nav class="nav">
      <div class="nav-item active">
        <svg viewBox="0 0 20 20"><circle cx="10" cy="10" r="9" fill="#5a3fe0"/><path d="M10 10 L14 6" stroke="#fff" stroke-width="2" stroke-linecap="round"/><circle cx="10" cy="10" r="1.8" fill="#fff"/></svg>
        DASHBOARD
      </div>
      <div class="nav-item">
        <svg viewBox="0 0 20 20"><path d="M11 2 L18 9 L9 18 L2 11 Z" fill="#1f1c4d"/><path d="M7 10 L10 13 M9 8 L12 11" stroke="#fff" stroke-width="1.4"/></svg>
        TICKETS
        <svg class="chev" viewBox="0 0 10 10"><path d="M2 3.5 L5 6.5 L8 3.5" fill="none" stroke="#6f6d80" stroke-width="1.3"/></svg>
      </div>
      <div class="nav-item">
        <svg viewBox="0 0 20 20"><path d="M2 9 L18 3 L13 17 L10 11 Z" fill="#1f1c4d"/><path d="M10 11 L18 3" stroke="#fff" stroke-width="1"/></svg>
        CONTACTS
      </div>
      <div class="nav-item">
        <svg viewBox="0 0 20 20"><circle cx="10" cy="10" r="6.5" fill="none" stroke="#1f1c4d" stroke-width="3.5" stroke-dasharray="3 2.1"/><circle cx="10" cy="10" r="4.5" fill="#1f1c4d"/><circle cx="10" cy="10" r="2" fill="#fff"/></svg>
        ADMIN SETTINGS
        <svg class="chev" viewBox="0 0 10 10"><path d="M2 3.5 L5 6.5 L8 3.5" fill="none" stroke="#6f6d80" stroke-width="1.3"/></svg>
      </div>
      <div class="nav-item">
        <svg viewBox="0 0 20 20"><rect x="2" y="2" width="16" height="6" rx="1" fill="#1f1c4d"/><rect x="5" y="8" width="10" height="10" fill="none" stroke="#1f1c4d" stroke-width="2"/><path d="M7 12 H13 M7 15 H13" stroke="#1f1c4d" stroke-width="1.4"/></svg>
        ACCOUNT &amp; BILLING
      </div>
    </nav>
    <div class="sidebar-art" role="img" aria-label="Soft abstract orange shapes decorating the sidebar"></div>
  </aside>

  <main class="main">
    <header class="topbar">
      <div class="crumbs">Dashboard<span class="sep">/</span>New Ticket</div>
      <div class="top-tools">
        <div class="search">Search
          <svg width="14" height="14" viewBox="0 0 14 14"><circle cx="6" cy="6" r="4.8" fill="none" stroke="#a9a8b5" stroke-width="1.2"/><path d="M9.5 9.5 L13 13" stroke="#a9a8b5" stroke-width="1.2"/></svg>
        </div>
        <div class="avatar">MO</div>
      </div>
    </header>

    <h1 class="page-title">New Ticket</h1>
    <p class="lead">The Contact will receive an email about this ticket.</p>

    <section class="form">
      <div class="row-to">To*
        <svg class="drop" width="10" height="10" viewBox="0 0 10 10"><path d="M2 3.5 L5 6.5 L8 3.5" fill="none" stroke="#6f6d80" stroke-width="1.3"/></svg>
        <span class="to-links">Add a Contact<span class="bar">|</span>cc<span class="bar">|</span>bcc</span>
      </div>
      <div class="row row-subject">Subject*</div>
      <div class="row row-meta">
        <div class="field"><label>Status</label><div class="select">Open<svg width="10" height="10" viewBox="0 0 10 10"><path d="M2 3.5 L5 6.5 L8 3.5" fill="none" stroke="#6f6d80" stroke-width="1.2"/></svg></div></div>
        <div class="field"><label>Priority</label><div class="select">Low<svg width="10" height="10" viewBox="0 0 10 10"><path d="M2 3.5 L5 6.5 L8 3.5" fill="none" stroke="#6f6d80" stroke-width="1.2"/></svg></div></div>
        <div class="field"><label>Groups</label><div class="select">Support<svg width="10" height="10" viewBox="0 0 10 10"><path d="M2 3.5 L5 6.5 L8 3.5" fill="none" stroke="#6f6d80" stroke-width="1.2"/></svg></div></div>
        <div class="field"><label>Agent</label><div class="select">Marta Olsen<svg width="10" height="10" viewBox="0 0 10 10"><path d="M2 3.5 L5 6.5 L8 3.5" fill="none" stroke="#6f6d80" stroke-width="1.2"/></svg></div></div>
      </div>
      <div class="row row-desc">Description*</div>
      <div class="row row-actions">
        <svg viewBox="0 0 20 20"><path d="M8 12 L12 8 M9 5 L11 3 A3.5 3.5 0 0 1 17 8 L15 10 M11 15 L9 17 A3.5 3.5 0 0 1 3 12 L5 10" fill="none" stroke="#5a3fe0" stroke-width="1.8" stroke-linecap="round"/></svg>
        <svg viewBox="0 0 20 20"><path d="M5 14 L10 2 L15 14 M7 10 H13" fill="none" stroke="#5a3fe0" stroke-width="1.8"/><path d="M3 18 H17" stroke="#5a3fe0" stroke-width="1.8"/></svg>
        <svg viewBox="0 0 20 20"><path d="M2 2 H18 V15 H9 L5 18 V15 H2 Z" fill="#5a3fe0"/><path d="M10 5 L11.2 7.6 L14 7.9 L11.9 9.7 L12.5 12.4 L10 11 L7.5 12.4 L8.1 9.7 L6 7.9 L8.8 7.6 Z" fill="#fff"/></svg>
        <div class="another"><span class="checkbox"></span>Create Another Ticket</div>
        <svg class="trash" width="12" height="14" viewBox="0 0 12 14"><rect x="2" y="3" width="8" height="11" rx="1" fill="#cfcfd6"/><rect x="1" y="1" width="10" height="1.5" fill="#cfcfd6"/></svg>
        <div class="btn-create">Create Ticket</div>
      </div>
      <div class="row row-tags">Tags <span class="tag-add">+Tag</span></div>
    </section>
  </main>
</div>
</body>
</html>
```